VFX Company Business Card Design Project

The Ember Vale is a decentralized Visual Effects Studio servicing the television and feature film industries.
Project Brief:
Take our logo that was previously designed on Pixel Harbor and make a double sided business card.
Requirements:
- Card MUST be double sided.
- Front of card MUST have the yellow part of our logo against the dark grey background.
- Back of card is completely up to the designer.
- Back of card must include the complete company logo.
Please follow these File Preparation guidelines:
http://printmoor.example/infopage?file=filetype_en&s=PrintMoor_new&lang=en
Industry/Entity Type
Business
Look and feel
Each slider illustrates characteristics of the customer's brand and the style your logo design should communicate.

```html
<!DOCTYPE html>
<html lang="en">
<head>
<meta charset="utf-8">
<title>The Ember Vale – Business Card</title>
<link rel="stylesheet" href="https://fonts.googleapis.com/css2?family=Ubuntu:wght@400;500;700&display=swap">
<style>
  :root {
    --backdrop: #d9dadb;
    --card-dark: #2a2b2c;
    --card-dark-edge: #333435;
    --band-grey: #5b6466;
    --accent-yellow: #f6c21c;
    --text-light: #f2f2f2;
    --logo-grey: #c9cfd1;
    --ink-dark: #1d1d1d;
  }
  * { box-sizing: border-box; margin: 0; padding: 0; }
  html, body { width: 1200px; height: 861px; overflow: hidden; }
  body {
    background: var(--backdrop);
    font-family: "Ubuntu", Arial, sans-serif;
    position: relative;
  }
  .card {
    position: absolute;
    top: 280px;
    width: 525px;
    height: 300px;
    background: linear-gradient(180deg, var(--card-dark-edge), var(--card-dark) 60%);
    overflow: hidden;
    box-shadow: 0 10px 30px rgba(0,0,0,0.25);
  }
  .card--front { left: 45px; }
  .card--back { left: 630px; }

  .brand {
    position: absolute;
    display: flex;
    align-items: center;
    gap: 14px;
    left: 50%;
    transform: translateX(-50%);
    white-space: nowrap;
  }
  .brand__dot {
    width: 40px; height: 40px;
    border-radius: 50%;
    background: var(--accent-yellow);
  }
  .brand__name {
    font-weight: 500;
    font-size: 34px;
    color: var(--logo-grey);
    letter-spacing: 0.5px;
  }
  .card--front .brand { top: 46px; }
  .card--back .brand { top: 112px; }
  .card--back .brand__dot { width: 48px; height: 48px; }
  .card--back .brand__name { font-size: 40px; }

  .name-tag {
    position: absolute;
    left: 26px; top: 138px;
    background: var(--accent-yellow);
    color: var(--ink-dark);
    font-weight: 500;
    font-size: 21px;
    padding: 5px 14px 6px 20px;
    border-radius: 0 6px 6px 0;
  }
  .position {
    position: absolute;
    left: 46px; top: 178px;
    font-size: 12px;
    font-weight: 500;
    color: var(--text-light);
  }

  .info-band {
    position: absolute;
    left: 0; right: 0; bottom: 0;
    background: var(--band-grey);
    border-top: 4px solid var(--accent-yellow);
  }
  .card--front .info-band { height: 92px; }
  .card--back .info-band { height: 76px; display: flex; align-items: center; justify-content: center; }

  .contact-list {
    position: absolute;
    list-style: none;
    top: 14px;
  }
  .contact-list--left { left: 26px; }
  .contact-list--right { left: 302px; top: 24px; }
  .contact-list li {
    display: flex;
    align-items: center;
    gap: 7px;
    height: 24px;
    font-size: 14px;
    color: var(--text-light);
  }
  .contact-icon { width: 15px; height: 15px; flex: none; }

  .website {
    font-size: 19px;
    font-weight: 500;
    color: var(--text-light);
  }
</style>
</head>
<body>

<section class="card card--front" aria-label="Business card front">
  <div class="brand">
    <span class="brand__dot"></span>
    <span class="brand__name">The Ember Vale</span>
  </div>

  <div class="name-tag">Name Surname</div>
  <div class="position">Position</div>

  <div class="info-band">
    <ul class="contact-list contact-list--left">
      <li>
        <svg class="contact-icon" viewBox="0 0 16 16" aria-hidden="true"><circle cx="8" cy="8" r="8" fill="#f2f2f2"/><rect x="5" y="4" width="6" height="8" fill="#5b6466"/></svg>
        123 Lorem Road, Ipsum City NY 456
      </li>
      <li>
        <svg class="contact-icon" viewBox="0 0 16 16" aria-hidden="true"><circle cx="8" cy="8" r="8" fill="#f2f2f2"/><path d="M5 11 L11 5" stroke="#5b6466" stroke-width="2.4" stroke-linecap="round"/></svg>
        123-456-789
      </li>
      <li>
        <svg class="contact-icon" viewBox="0 0 16 16" aria-hidden="true"><circle cx="8" cy="8" r="8" fill="#f2f2f2"/><rect x="5.5" y="3.5" width="5" height="9" rx="1" fill="#5b6466"/></svg>
        123-456-789
      </li>
    </ul>
    <ul class="contact-list contact-list--right">
      <li>
        <svg class="contact-icon" viewBox="0 0 16 16" aria-hidden="true"><circle cx="8" cy="8" r="8" fill="#f2f2f2"/><rect x="4" y="5" width="8" height="6" fill="#5b6466"/><path d="M4 5 L8 8.5 L12 5" stroke="#f2f2f2" stroke-width="1" fill="none"/></svg>
        email@yourdomain.com
      </li>
      <li>
        <svg class="contact-icon" viewBox="0 0 16 16" aria-hidden="true"><circle cx="8" cy="8" r="8" fill="#f2f2f2"/><rect x="4" y="4.5" width="8" height="7" fill="#5b6466"/><rect x="4" y="4.5" width="8" height="1.8" fill="#2a2b2c"/></svg>
        www.yourdomain.com
      </li>
    </ul>
  </div>
</section>

<section class="card card--back" aria-label="Business card back">
  <div class="brand">
    <span class="brand__dot"></span>
    <span class="brand__name">The Ember Vale</span>
  </div>
  <div class="info-band">
    <span class="website">www.yourdomain.com</span>
  </div>
</section>

</body>
</html>
```